Manufacturing business needs a website revamp

We are a manufacturing business supplying parts and modules to mid-high end consumer electronics brands from kitchen appliances to powered tools mainly in US/Europe. We want design ideas for a revamp of our website. We're aiming for a look and feel that's sleek, tidy and modern whilst still providing the right balance for content. A smooth and comfortable user experience that directs users to the information they may be looking for and promote our services. Something that incorporates design ideas such as: responsive design, lazy loading, slider banners, responsive layout, dynamic scrolling, liquid layout, full page headers etc... These are just terms bounced around within our team and certainly neither exclusive nor absolutely necessary. This is our current website for reference: https://www.valmoriqtech.com/ , which we feel is both outdated and doesn't engage visitors.

Attached is our planned new site map (we’re open to additional ideas here). We would like mock ups for each page on the site map. We will subsequently fill out the contents ourselves, but require design directions on e.g. how much text should go at which spot. E.g. for our Automotive page under Industries, we would like a suitable layout to be designed, as well as designated areas for texts. As for assets, please use any of the assets already on our current site or external source. We’ve yet to finalize on our selection of assets so please use the above as placeholders for now. Additionally, we would want a mock up for a pop-up frame to showcase additional technical specifications for some of our product ranges. For example, under the powertools section of our current website, we have additional listings under our product range. Currently they do not have a pop up function, but if we were to create a pop up frame to display detailed specifications, what layout should we use?

Finally, our target audiences are professional representatives from leading consumer brands who may be interested in our services. Our target customers are mid-high end brands. Think, for example, KRV/Halvorne for automotive, Quenmatic/Pruvet/Tolvaro for consumer electronics/kitchen appliances, and Marwick Fenn & Toller/Caddowin for powered tools. Typically it will be their product designers/engineers and supply chain representatives who will visit our website.

Target Market(s)

Professional product engineers/designers from mid-high end consumer electronics brands.

Industry/Entity Type

Manufacturing

Contact Information for Business Card

Attached are back and front of our current name card design. Again, we're open to changes that matches the style of our future website design. A few notes on the business card design:
- Cannot have blue background
- Does not have to be bilingual. I.e. open to single language design on one side and logo on the other

Coding

Coded - Design and coding required

Number of Pages Required

5+ page

Font styles to use
Sans Serif

Colors
3176b5

Requirements
Must have
• Color scheme must be based on the blue from our current website design. We will be keeping our current logo, hence must match that logo.
Nice to have
• Wix (or similar platforms) as demos/final solutions ok.
Should not have
• See brief

```html
<!DOCTYPE html>
<html lang="en">
<head>
<meta charset="utf-8">
<title>Valmoriq — Milestones</title>
<link href="https://fonts.googleapis.com/css2?family=Open+Sans:wght@400;600;700&display=swap" rel="stylesheet">
<style>
:root{
  --navy:#000c2b;
  --navy-head:#00102f;
  --accent:#3a9be2;
  --band:#42a7e6;
  --white:#ffffff;
  --muted:#c9d3e3;
  --bar:#0a0a0f;
}
*{margin:0;padding:0;box-sizing:border-box}
html,body{width:1200px;height:2250px;overflow:hidden}
body{position:relative;background:var(--white);font-family:"Open Sans",Arial,sans-serif;color:var(--white)}
.abs{position:absolute}
.site-header{left:0;top:0;width:1200px;height:98px;background:var(--navy-head)}
.brand{left:28px;top:20px;display:flex;align-items:center;gap:12px}
.brand-mark{width:42px;height:42px;background:var(--accent)}
.brand-text{display:flex;flex-direction:column}
.brand-name{font-size:38px;font-weight:700;line-height:40px;color:var(--white)}
.brand-tag{font-size:9px;font-weight:400;color:var(--white);margin-left:12px}
.nav{top:36px;font-size:16px;font-weight:700}
.nav a{position:absolute;color:var(--white);text-decoration:none;white-space:nowrap}
.nav a.active{color:var(--accent)}
.lang{left:1052px;top:39px;display:flex;align-items:center;gap:5px;font-size:11px}
.hero{left:0;top:98px;width:1200px;height:400px;background:radial-gradient(circle at 75% 30%,#b9d6e6 0%,#5e8fb0 30%,#1f4766 65%,#0e2a44 100%)}
.hero-title{left:188px;top:392px;font-size:62px;font-weight:700;line-height:70px}
.intro{left:0;top:498px;width:1200px;height:224px;background:var(--navy)}
.intro h2{position:absolute;left:189px;top:36px;font-size:31px;font-weight:700;color:var(--accent)}
.intro p{position:absolute;left:189px;top:102px;width:735px;font-size:15.5px;line-height:25px;color:var(--white)}
.card{position:absolute;background:var(--navy);border-left:5px solid var(--accent);padding:28px 24px 0 22px}
.card .year{font-size:45px;font-weight:700;color:var(--accent);line-height:52px}
.card .note{margin-top:18px;font-size:17.5px;font-weight:700;line-height:25px}
.card .note.tight{white-space:nowrap}
.contact{left:0;top:1770px;width:1200px;height:129px;background:var(--band)}
.contact .label{position:absolute;top:36px;font-size:15px}
.contact .value{position:absolute;top:61px;font-size:19px;font-weight:700}
.footer{left:0;top:1899px;width:1200px;height:299px;background:var(--navy)}
.footer .col{position:absolute;top:38px;font-size:15px;line-height:29px;color:var(--muted)}
.footer h4{font-size:15px;font-weight:700;color:var(--muted);line-height:20px}
.footer .rule{height:1px;background:#3a4a6a;margin:7px 0 14px}
.footer .company{font-weight:700}
.social{font-size:13px;line-height:25px;display:flex;flex-direction:column}
.social span{display:flex;align-items:center;gap:10px}
.social i{width:9px;height:9px;border-radius:50%;background:var(--muted);display:inline-block}
.bottom{left:0;top:2198px;width:1200px;height:52px;background:var(--bar);font-size:12px;color:var(--muted)}
.bottom .copy{position:absolute;left:140px;top:15px}
.bottom .legal{position:absolute;right:99px;top:13px;font-size:11px}
</style>
</head>
<body>
<header class="abs site-header">
  <div class="abs brand">
    <div class="brand-mark"></div>
    <div class="brand-text">
      <span class="brand-name">Valmoriq</span>
      <span class="brand-tag">Building Parts That Last Long</span>
    </div>
  </div>
  <nav class="abs nav" style="left:0;width:1200px">
    <a class="active" style="left:546px">About Us</a>
    <a style="left:647px">Industries</a>
    <a style="left:762px">Core Competencies</a>
    <a style="left:949px">News</a>
  </nav>
  <div class="abs lang">
    <svg width="15" height="15" viewBox="0 0 16 16" fill="none" stroke="#fff" stroke-width="1.2"><circle cx="8" cy="8" r="7"/><ellipse cx="8" cy="8" rx="3" ry="7"/><path d="M1 8h14M2.5 4.5h11M2.5 11.5h11"/></svg>
    <span>Select language</span>
    <svg width="8" height="8" viewBox="0 0 8 8" fill="none" stroke="#fff" stroke-width="1.4"><path d="M1 2.5l3 3 3-3"/></svg>
  </div>
</header>

<section class="abs hero" role="img" aria-label="Photo of a businessman's hand pointing at a glowing upward growth arrow over rising bars">
</section>
<h1 class="abs hero-title">Milestones</h1>

<section class="abs intro">
  <h2>Our History, Your Strength</h2>
  <p>Lorem ipsum dolor sit amet, consectetur adipiscing elit, sed do eiusmod tempor incididunt ut labore et dolore magna aliqua. Ut enim ad minim veniam, quis nostrud exercitation ullamco laboris nisi ut aliquip ex ea commodo consequat.</p>
</section>

<main class="timeline">
  <div class="card" style="left:32px;top:760px;width:404px;height:224px"><div class="year">2019</div><div class="note">Awarded Certificate of Integration of Informatization and Industrialization Assessment (GB/T 23001-2017)</div></div>
  <div class="card" style="left:455px;top:760px;width:292px;height:224px"><div class="year">2017</div><div class="note">Established dedicated<br>R&amp;D center</div></div>
  <div class="card" style="left:766px;top:760px;width:399px;height:224px"><div class="year">2013</div><div class="note">Implemented Intelligent<br>Manufacturing Control</div></div>

  <div class="card" style="left:32px;top:1002px;width:229px;height:224px"><div class="year">2012</div><div class="note">Launched Industry<br>4.0 initiative</div></div>
  <div class="card" style="left:280px;top:1002px;width:312px;height:224px;padding-top:36px"><div class="year">2011</div><div class="note">Upgraded Automation and<br>LEAN manufacturing</div></div>
  <div class="card" style="left:617px;top:1002px;width:256px;height:224px;padding-right:6px"><div class="year">2010</div><div class="note tight">Restructured Mainland<br>China corporate entity</div></div>
  <div class="card" style="left:895px;top:1002px;width:268px;height:224px;padding-left:34px"><div class="year">2006</div><div class="note">Acquired Kelmar<br>Automotive GmbH</div></div>

  <div class="card" style="left:32px;top:1246px;width:311px;height:225px;padding-top:36px;padding-left:30px"><div class="year">2000</div><div class="note">Awarded TS16949<br>certification</div></div>
  <div class="card" style="left:368px;top:1246px;width:386px;height:225px;padding-left:30px;padding-top:32px"><div class="year">1990</div><div class="note">Formed joint ventures with<br>renowned Italian and Swiss<br>switches manufacturers</div></div>
  <div class="card" style="left:778px;top:1246px;width:387px;height:225px;padding-left:37px;padding-top:18px"><div class="year">1988</div><div class="note">Rose To Become The Top<br>Hong Kong Home Appliance<br>Switches Supplier</div></div>

  <div class="card" style="left:32px;top:1494px;width:555px;height:224px;padding-left:28px"><div class="year">1984</div><div class="note">Established first Mainland<br>China manufacturing base</div></div>
  <div class="card" style="left:610px;top:1494px;width:555px;height:224px;padding-left:29px;padding-top:30px"><div class="year">1978</div><div class="note" style="margin-top:8px">Valmoriq Electech traces its origins to 1978, when the<br>Parent Company was established in Hong Kong</div></div>
</main>

<section class="abs contact">
  <span class="label" style="left:147px">Do you have any questions?</span>
  <span class="value" style="left:147px">Contact us.</span>
  <span class="label" style="left:451px">Phone number</span>
  <span class="value" style="left:451px">(86) 0755-41839260</span>
  <span class="label" style="left:764px">Email</span>
  <span class="value" style="left:764px">BD@valmoriqtech.com</span>
</section>

<footer class="abs footer">
  <div class="col" style="left:140px;top:36px">
    <div class="company">Valmoriq Electech Co., Ltd</div>
    <div>The 3rd Industrial Area,</div>
    <div>Lanshan Town, Fenhe City</div>
    <div>Qingmu Province, PRC</div>
    <div style="margin-top:28px">Tel: (86) 0755-41839260</div>
    <div>Fax: (86) 0755-41839288</div>
    <div>Email: BD@valmoriqtech.com</div>
  </div>
  <div class="col" style="left:451px;width:140px">
    <h4>About Us</h4><div class="rule"></div>
    <div>Vision and Mission</div><div>Milestones</div><div>Contact Us</div><div>Careers</div>
  </div>
  <div class="col" style="left:652px;width:139px">
    <h4>Industries</h4><div class="rule"></div>
    <div>Automotive</div><div>Home Appliances</div><div>Power Tools</div>
  </div>
  <div class="col" style="left:894px;width:128px">
    <h4>Follow Us on</h4><div class="rule" style="margin-bottom:8px"></div>
    <div class="social">
      <span><i></i>Linkwall</span>
      <span><i></i>Chatterly</span>
      <span><i></i>Picturefeed</span>
    </div>
  </div>
</footer>

<div class="abs bottom">
  <span class="copy">Copyright © 2020 Valmoriq. All rights reserved.</span>
  <span class="legal">Privacy Policy | Terms &amp; Conditions</span>
</div>
</body>
</html>
```